Need a flyer and a web page so I can have tourists come into my restaurant

First need to design a flyer that brings the Puerto Rico tourists to my restaurant I will send logo and menu needs to be in english the flyer. I willleave flyer at hotels and geust houses and tour guide companies.
Casa Ordiales
3817 Calle Tamarindal
Punta Las Marías
San Juan, PR 000912
email: Casaordialespr@mailvento.com
Tel (787) 555-0143

```html
<!DOCTYPE html>
<html lang="en">
<head>
<meta charset="utf-8">
<title>Casa Ordiales — Flyer, Side 1 and Side 2</title>
<link href="https://fonts.googleapis.com/css2?family=Source+Sans+3:ital,wght@0,400;0,600;1,400;1,600&family=Allura&family=Noto+Serif:ital@1&display=swap" rel="stylesheet">
<style>
  :root{
    --backdrop:#e4e4e2;
    --label:#7a7a7a;
    --teal-band:#1fb8cc;
    --card:#fbfbf7;
    --teal-text:#1c9fbf;
    --green:#8cc63f;
    --logo:#3f93ad;
    --caption:#8a8a8a;
    --frame:#fdfdfb;
  }
  *{margin:0;padding:0;box-sizing:border-box}
  html,body{width:1200px;height:930px;overflow:hidden;background:var(--backdrop)}
  body{position:relative;font-family:"Source Sans 3",Arial,sans-serif}

  .side-label{position:absolute;top:58px;font-family:"Noto Serif",Georgia,serif;font-style:italic;font-size:19px;color:var(--label)}
  .side-label--one{left:279px}
  .side-label--two{left:846px}

  .flyer{position:absolute;top:113px;width:527px;height:747px;background:var(--teal-band);box-shadow:4px 6px 8px rgba(0,0,0,.25)}
  .flyer--one{left:38px}
  .flyer--two{left:618px}
  .flyer__card{position:absolute;left:20px;top:20px;width:485px;height:705px;background:var(--card);border-radius:9px}

  .logo{position:absolute;left:250px;top:18px;width:230px;color:var(--logo);font-weight:400;line-height:1;display:flex;flex-direction:column;align-items:flex-start}
  .logo__top{font-size:32px;margin-left:6px}
  .logo__name{font-size:48px;margin-left:40px;margin-top:0}

  .headline{position:absolute;left:19px;color:var(--green);font-weight:600;font-style:italic;z-index:2}
  .flyer--one .headline{top:15px;font-size:19.5px;line-height:24.5px}
  .flyer--two .headline{top:14px;font-size:25px;line-height:28px}

  .copy{position:absolute;left:19px;color:var(--teal-text);z-index:2}
  .copy p+p{margin-top:7px}
  .copy em{font-style:italic}
  .flyer--one .copy{top:92px;width:218px;font-size:13.5px;line-height:15.9px}
  .flyer--two .copy{top:79px;width:218px;font-size:15.5px;line-height:19.8px;font-weight:600}

  .snapshot{position:absolute;background:var(--frame);box-shadow:2px 3px 7px rgba(0,0,0,.28);padding:14px 14px 0}
  .snapshot__photo{width:100%;border-radius:8px;border:1px solid #cfcfcf}
  .snapshot__caption{font-family:"Allura",cursive;color:var(--caption);font-size:19px;line-height:1.2;text-align:center;white-space:nowrap;padding-top:8px;margin:0 -8px}

  .contact{position:absolute;left:20px;top:595px;width:445px;height:94px;background:var(--green);border:3px solid #fff;
    clip-path:polygon(14px 0,calc(100% - 14px) 0,100% 14px,100% calc(100% - 14px),calc(100% - 14px) 100%,14px 100%,0 calc(100% - 14px),0 14px);
    color:#fff;text-align:center;font-size:16.5px;line-height:21px;padding-top:5px}
  .contact-shadow{position:absolute;left:22px;top:598px;width:445px;height:94px;background:rgba(0,0,0,.15);filter:blur(3px);
    clip-path:polygon(14px 0,calc(100% - 14px) 0,100% 14px,100% calc(100% - 14px),calc(100% - 14px) 100%,14px 100%,0 calc(100% - 14px),0 14px)}
  .contact em{font-style:italic}
</style>
</head>
<body>
  <div class="side-label side-label--one">Side 1</div>
  <div class="side-label side-label--two">Side 2</div>

  <section class="flyer flyer--one">
    <div class="flyer__card">
      <h1 class="headline">Casa Ordiales is a<br>great place to relax and<br>have a wonderful dinner.</h1>
      <div class="logo"><span class="logo__top">Casa</span><span class="logo__name">Ordiales</span></div>

      <div class="copy">
        <p>We serve mediterranean cuisine and tipical Puerto-Rican food, and also fusion of both of them, making some delicious new plates like our risotto with gandules and carne ahumada, smoked with mango and guava wood, desserts made here in-house, fresh lobster from Puerto Rico and the best osso buco you'll ever have!</p>
        <p><em>And make sure you try our famous Watermelon Sangria and Frozen Mojito!</em></p>
        <p>We are a family operated restaurant and our service is very high quality - come on over and be the judge of it. You will enjoy an artwork exposition by the famous Puerto-Rican painter and artist Andrés Ordiales.</p>
      </div>

      <figure class="snapshot" style="left:238px;top:128px;width:256px;height:280px;transform:rotate(3deg)">
        <div class="snapshot__photo" role="img" aria-label="Photo of the dining room with paintings on the walls" style="height:226px;background:linear-gradient(180deg,#d9d2c4 0%,#b7a58c 45%,#6e5a48 100%)"></div>
        <figcaption class="snapshot__caption">Our dining room and artworks exposition</figcaption>
      </figure>

      <figure class="snapshot" style="left:6px;top:400px;width:212px;height:176px;transform:rotate(-3deg)">
        <div class="snapshot__photo" role="img" aria-label="Street map marking the restaurant location" style="height:124px;background:linear-gradient(135deg,#ecebe6 0%,#dedbd2 60%,#c8dbe6 100%)"></div>
        <figcaption class="snapshot__caption">Our location on the map</figcaption>
      </figure>

      <figure class="snapshot" style="left:234px;top:405px;width:233px;height:176px">
        <div class="snapshot__photo" role="img" aria-label="The painter standing in front of a large abstract painting" style="height:124px;background:linear-gradient(180deg,#c9c4b6 0%,#7f7a45 40%,#6a3d2e 75%,#8a6e5a 100%)"></div>
        <figcaption class="snapshot__caption">Maestro Ordiales</figcaption>
      </figure>

      <div class="contact-shadow"></div>
      <div class="contact">
        3817 Calle Tamarindal, Punta Las Marias, San Juan, PR 00912<br>
        <em>Open hours:</em> Thursday to Sunday, 11am - 11pm<br>
        Phone: (787) 555-0143<br>
        <em>E-mail:</em> Casaordialespr@mailvento.com
      </div>
    </div>
  </section>

  <section class="flyer flyer--two">
    <div class="flyer__card">
      <h2 class="headline">Come on over<br>and be our guest.</h2>
      <div class="logo"><span class="logo__top">Casa</span><span class="logo__name">Ordiales</span></div>

      <div class="copy">
        <p>You'll enjoy our delicious food, cozy atmosphere, very high quality service and artworks by the famous painter and artist Andrés Ordiales.</p>
      </div>

      <figure class="snapshot" style="left:-10px;top:196px;width:226px;height:176px;transform:rotate(-1deg)">
        <div class="snapshot__photo" role="img" aria-label="Plated bacalao with peppers" style="height:124px;background:radial-gradient(ellipse at 50% 55%,#9aa85a 0%,#e9e4da 45%,#f4f2ee 100%)"></div>
        <figcaption class="snapshot__caption">Bacalao Riojana</figcaption>
      </figure>

      <figure class="snapshot" style="left:222px;top:128px;width:266px;height:280px;transform:rotate(3deg)">
        <div class="snapshot__photo" role="img" aria-label="Full dining room with guests and hanging colourful banners" style="height:226px;background:linear-gradient(180deg,#c9bcae 0%,#8a6a4e 40%,#3e2b22 100%)"></div>
        <figcaption class="snapshot__caption">Friendly atmosphere &amp; great food</figcaption>
      </figure>

      <figure class="snapshot" style="left:-4px;top:402px;width:236px;height:176px;transform:rotate(-4deg)">
        <div class="snapshot__photo" role="img" aria-label="Grilled Caribbean lobster plate" style="height:124px;background:linear-gradient(160deg,#3a2a22 0%,#b5472e 45%,#d9b07a 70%,#2e2420 100%)"></div>
        <figcaption class="snapshot__caption">Caribbean Lobster</figcaption>
      </figure>

      <figure class="snapshot" style="left:247px;top:404px;width:233px;height:176px">
        <div class="snapshot__photo" role="img" aria-label="Ossobuco with sauce over pasta" style="height:124px;background:radial-gradient(ellipse at 50% 50%,#6e4320 0%,#b08a58 45%,#eeebe3 80%)"></div>
        <figcaption class="snapshot__caption">Best Ossobuco you'll ever have!</figcaption>
      </figure>

      <div class="contact-shadow"></div>
      <div class="contact">
        3817 Calle Tamarindal, Punta Las Marias, San Juan, PR 00912<br>
        <em>Open hours:</em> Thursday to Sunday, 11am - 11pm<br>
        Phone: (787) 555-0143<br>
        <em>E-mail:</em> Casaordialespr@mailvento.com
      </div>
    </div>
  </section>
</body>
</html>
```